Law firm Seeks Modern and Engaging Site Redesign

Law firm seeks a new web site. Should be modern, but retaining existing logo. Needs to include contact section, professional bio, services offered, and contact information.

The site should be modern, responsive, and able to be SEO optimized.

The finished product should be coded in a Wordpress site, which I will provide. I can work with other platforms, including Wix, but WP is preferred.

Note the current site is https://www.tallowfieldlaw.example/#/home

Target Market(s)

Family Law Practice

Industry/Entity Type

Legal

Coding

Coded - Design and coding required

Number of Pages Required

4 page

Font styles to use
Sans Serif

Requirements
Must have
• Service description
Bio pages for partners
Contact Form
Awards/Publication page

```html
<!DOCTYPE html>
<html lang="en">
<head>
<meta charset="utf-8">
<title>Tallowfield Marsh — Attorneys at Law</title>
<link rel="stylesheet" href="https://fonts.googleapis.com/css2?family=Josefin+Sans:wght@300;400;600;700&family=League+Spartan:wght@600;700;800&display=swap">
<style>
:root{
  --navy:#272a3b;
  --ink:#15161c;
  --blue:#3e4f9f;
  --link:#4a6fd4;
  --paper:#ffffff;
  --mist:#f4f4f4;
  --sand:#f0efeb;
  --grey:#7a7a80;
  --line:#d9d9dd;
  --footer:#23242f;
  --photo-dark:#2e3040;
  --photo-warm:#8a6a4a;
}
*{margin:0;padding:0;box-sizing:border-box}
html,body{width:1200px;height:5333px;overflow:hidden}
body{position:relative;background:var(--paper);font-family:"Josefin Sans",sans-serif;color:var(--ink)}
.abs{position:absolute}
.head{font-family:"League Spartan",sans-serif;font-weight:800;text-transform:uppercase;line-height:1}
.photo{position:absolute}

/* header */
.site-header{position:absolute;left:0;top:0;width:1200px;height:104px;background:var(--paper)}
.nav{position:absolute;top:44px;display:flex;gap:26px;font-size:13px;letter-spacing:.5px}
.nav a{color:var(--ink);text-decoration:none}
.nav a.active{color:var(--link)}
.brand{position:absolute;left:0;width:1200px;top:26px;text-align:center}
.brand-name{font-size:30px;font-weight:400;color:#55596b;letter-spacing:.5px}
.brand-tag{font-size:11px;color:var(--link);margin-top:2px;padding-left:120px}
.social{position:absolute;display:flex;gap:12px}
.social span{width:10px;height:10px;border-radius:50%;background:var(--ink);display:block}

/* hero */
.hero{position:absolute;left:0;top:104px;width:1200px;height:641px;background:var(--navy)}
.hero-title{position:absolute;left:420px;top:64px;font-family:"Josefin Sans",sans-serif;font-weight:700;font-size:62px;letter-spacing:14px;line-height:68px;color:#e9e9ee;text-transform:uppercase}
.hero-title span{color:#8d8f99}
.hero-text{position:absolute;left:788px;top:326px;width:270px;font-size:16.5px;line-height:29px;color:#fff}
.btn{position:absolute;background:var(--blue);color:#fff;font-size:12px;font-weight:700;letter-spacing:3px;text-transform:uppercase;display:flex;align-items:center;justify-content:center}
.hero-arrow{position:absolute;width:36px;height:36px;border-radius:50%;background:rgba(255,255,255,.12)}

/* about */
.eyebrow{position:absolute;font-size:16px;color:#444}
.who-box{position:absolute;left:700px;top:993px;width:500px;height:534px;background:var(--mist)}
.who-title{position:absolute;left:631px;top:1078px;font-size:48px;letter-spacing:1px;color:#3a3a3e;font-family:"League Spartan",sans-serif;font-weight:800}
.who-title em{font-style:normal;color:#8a8a8f}
.who-text{position:absolute;left:735px;top:1138px;width:370px;font-size:16.5px;line-height:30px;color:#333}

/* services */
.center{position:absolute;left:0;width:1200px;text-align:center}
.svc-title{position:absolute;font-family:"League Spartan",sans-serif;font-weight:800;font-size:30px;color:#9a9a9f;text-transform:uppercase;letter-spacing:.5px}
.learn{position:absolute;font-size:16px;color:#222}
.rule{position:absolute;height:2px;width:26px;background:var(--ink)}

/* team */
.member-name{position:absolute;font-size:18px;color:#222}
.member-rate{position:absolute;font-size:13px;color:#666}

/* stats */
.stats{position:absolute;left:0;top:2766px;width:1200px;height:466px;background:linear-gradient(135deg,#1d1a1c,#3a2a24 45%,#1b1b22)}
.stat{position:absolute;width:240px;text-align:center;color:#fff}
.stat b{display:block;font-family:"League Spartan",sans-serif;font-weight:700;font-size:52px;line-height:1}
.stat i{display:block;font-style:normal;font-family:"League Spartan",sans-serif;font-weight:700;font-size:18px;margin-top:12px}

/* testimonials */
.testi{position:absolute;left:0;top:3232px;width:1200px;height:881px;background:var(--sand)}
.card{position:absolute;background:#fff;box-shadow:0 6px 20px rgba(0,0,0,.05)}
.quote{position:absolute;left:340px;top:3660px;width:520px;text-align:center;font-size:17px;line-height:33px;color:#333}
.quote-mark{position:absolute;left:560px;top:3610px;font-size:110px;color:#ececec;font-family:Georgia,serif;line-height:1}

/* consult */
.consult{position:absolute;left:0;top:4113px;width:1200px;height:356px;background:linear-gradient(90deg,#1f2029,#2b2c36 55%,#3a2f28)}

/* contact */
.field-label{position:absolute;font-size:13px;color:#444}
.field-line{position:absolute;height:1px;background:var(--line)}
.map{position:absolute;left:811px;top:4577px;width:389px;height:513px;background:linear-gradient(160deg,#e8eee6,#dfe8dc 50%,#cfe0f0)}

/* footer */
.footer{position:absolute;left:0;top:5090px;width:1200px;height:243px;background:var(--footer);color:#c9c9cf}
.foot-small{position:absolute;font-size:12.5px;line-height:24px;color:#b9bac2}
.foot-social{position:absolute;left:883px;top:5166px;display:flex;gap:20px}
.foot-social span{width:12px;height:12px;border-radius:50%;background:#fff;display:block}
</style>
</head>
<body>

<header class="site-header">
  <nav class="nav" style="left:108px">
    <a class="active" href="#">HOME</a><a href="#">ABOUT</a><a href="#">SERVICES</a><a href="#">TEAM</a>
  </nav>
  <div class="brand">
    <div class="brand-name">Tallowfield Marsh</div>
    <div class="brand-tag">Attorneys at Law</div>
  </div>
  <nav class="nav" style="left:866px">
    <a href="#">BLOG</a><a href="#">CONTACT</a>
  </nav>
  <div class="social" style="left:1024px;top:46px"><span></span><span></span><span></span></div>
</header>

<section class="hero">
  <div class="photo" role="img" aria-label="Photo of a gavel, scales of justice and open law book on a desk" style="left:0;top:153px;width:720px;height:488px;background:linear-gradient(160deg,#2d3145 0%,#3b3a40 45%,#7a5a3c 80%,#5a4230 100%)"></div>
  <div class="hero-arrow" style="left:28px;top:378px"></div>
  <div class="hero-arrow" style="left:654px;top:378px"></div>
  <h1 class="hero-title">When<br>Experience<br>Matters <span>most!</span></h1>
  <p class="hero-text">The law firm of Tallowfield Marsh, LLC is based in Alder County, conveniently located in Riverton, New Jersey in 40 Commerce Plaza...</p>
  <a class="btn" style="left:788px;top:492px;width:170px;height:41px">Learn More</a>
</section>

<div class="eyebrow" style="left:110px;top:800px">About Us</div>
<h2 class="head abs" style="left:110px;top:838px;font-size:68px;line-height:76px">About<br>the Firm</h2>

<div class="who-box"></div>
<div class="photo" role="img" aria-label="Portrait of the two founding partners in dark suits" style="left:0;top:1028px;width:700px;height:453px;background:radial-gradient(ellipse at 45% 55%,#4a4f63 0%,#2d3042 55%,#262838 100%)"></div>
<h2 class="who-title">WHO <em>WE</em> ARE</h2>
<p class="who-text">The law firm of Tallowfield Marsh, LLC is based in Alder County, conveniently located in Riverton, New Jersey in 40 Commerce Plaza. We serve the needs of clients throughout Alder County, as well as, clients from several other counties, including, but not limited to, Linden, Marlow, Ashby and Fenwick. Between our partners, we have over 30+ years of experience assisting clients with all of their family law and criminal law needs.</p>

<div class="center" style="top:1650px;font-size:17px;color:#333">LAW</div>
<h2 class="center head" style="top:1682px;font-size:48px">Services</h2>

<div class="photo" role="img" aria-label="Photo of a lawyer meeting a client in an office" style="left:126px;top:1773px;width:466px;height:255px;background:linear-gradient(120deg,#3a3a42,#6d6a66 50%,#a88a66)"></div>
<div class="photo" role="img" aria-label="Photo of a distressed client with a lawyer beside scales of justice" style="left:623px;top:1773px;width:465px;height:255px;background:linear-gradient(120deg,#bfbab2,#8e8a86 55%,#c9b592)"></div>
<div class="svc-title" style="left:108px;top:2012px">Family Law</div>
<div class="learn" style="left:108px;top:2058px">Learn More</div>
<div class="rule" style="left:108px;top:2085px"></div>
<div class="svc-title" style="left:607px;top:2012px">Criminal Law</div>
<div class="learn" style="left:607px;top:2058px">Learn More</div>
<div class="rule" style="left:607px;top:2085px"></div>

<div class="eyebrow" style="left:108px;top:2202px">Lorem ipsum dolor sit</div>
<h2 class="head abs" style="left:108px;top:2236px;font-size:64px">Our Team</h2>
<a class="btn" style="left:859px;top:2251px;width:233px;height:41px;font-size:11px">View All Members</a>

<div class="photo" role="img" aria-label="Portrait of partner Daniel R. Tallowfield" style="left:110px;top:2344px;width:228px;height:226px;background:linear-gradient(180deg,#5a5c66,#2c2f3f)"></div>
<div class="photo" role="img" aria-label="Portrait of partner Owen P. Marsh" style="left:360px;top:2344px;width:226px;height:226px;background:linear-gradient(180deg,#6a6a70,#2b2d38)"></div>
<div class="photo" role="img" aria-label="Portrait of attorney Lena M. Ortiz" style="left:610px;top:2344px;width:228px;height:226px;background:linear-gradient(180deg,#9a8a86,#3a3a40)"></div>
<div class="photo" role="img" aria-label="Portrait of attorney Clara J. Whitcombe" style="left:859px;top:2344px;width:228px;height:226px;background:linear-gradient(180deg,#ffffff 40%,#2f55b8)"></div>

<div class="member-name" style="left:110px;top:2588px">Daniel R. Tallowfield</div>
<div class="member-rate" style="left:110px;top:2622px">Rated By TopCounsel</div>
<div class="member-name" style="left:360px;top:2588px">Owen P. Marsh</div>
<div class="member-rate" style="left:360px;top:2622px">Rated By TopCounsel</div>
<div class="member-name" style="left:610px;top:2588px">Lena M. Ortiz</div>
<div class="member-rate" style="left:610px;top:2622px">Rated By TopCounsel</div>
<div class="member-name" style="left:859px;top:2588px">Clara J. Whitcombe</div>
<div class="member-rate" style="left:859px;top:2622px">Rated By TopCounsel</div>

<section class="stats" role="img" aria-label="Dark background photo of a wooden gavel">
  <div class="stat" style="left:108px;top:182px"><b>123+</b><i>Happy Customers</i></div>
  <div class="stat" style="left:377px;top:182px"><b>234+</b><i>Finished Project</i></div>
  <div class="stat" style="left:606px;top:182px"><b>50+</b><i>Partners</i></div>
  <div class="stat" style="left:859px;top:182px"><b>4+</b><i>Team Members</i></div>
</section>

<section class="testi"></section>
<div class="abs" style="left:271px;top:3384px;width:656px;height:54px;background:#e3e2df"></div>
<h2 class="center head" style="top:3366px;font-size:64px;line-height:84px">What Clients Say<br>About Us</h2>
<div class="card" style="left:335px;top:3600px;width:530px;height:338px"></div>
<div class="card" style="left:300px;top:3580px;width:598px;height:343px"></div>
<div class="card" style="left:271px;top:3555px;width:656px;height:362px"></div>
<div class="quote-mark">&ldquo;</div>
<p class="quote">Lorem ipsum dolor sit amet, consectetur adipiscing elit, sed do eiusmod tempor incididunt ut labore et dolore magna aliqua. Ut enim ad minim veniam, quis nostrud exercitation ullamco laboris nisi ut aliquip ex ea commodo consequat. Duis aute irure dolor in</p>
<div class="center" style="top:3824px;font-size:12px;font-weight:700">JOHN DOE</div>
<div class="center" style="top:3846px;font-size:12px;color:#a5a7c0">Senior Designer, Squre.</div>
<svg class="abs" style="left:560px;top:4020px" width="82" height="20" viewBox="0 0 82 20" fill="none" stroke="#555" stroke-width="2">
  <path d="M32 10H4M10 4L4 10l6 6"/><path d="M50 10h28M72 4l6 6-6 6"/>
</svg>

<section class="consult" role="img" aria-label="Dark photo of a gavel on a desk">
  <h2 class="head abs" style="left:112px;top:150px;font-size:32px;color:#fff;font-weight:700">Schedule a Consultation</h2>
  <p class="abs" style="left:112px;top:202px;width:460px;font-size:16.5px;line-height:25px;color:#fff">Lorem ipsum dolor sit amet, consectetur adipiscing elit, sed do eiusmod tempor incididunt ut labore et dolore</p>
  <a class="btn" style="left:869px;top:164px;width:170px;height:41px;font-size:11px">Contact Us</a>
</section>

<div class="eyebrow" style="left:108px;top:4548px">Lorem ipsum dolor sit</div>
<h2 class="head abs" style="left:108px;top:4584px;font-size:64px">Contact Us</h2>
<div class="eyebrow" style="left:108px;top:4664px;font-size:16.5px">Lorem ipsum dolor sit amet, consectetur adipiscing elit, sed do eiusmod</div>

<div class="field-label" style="left:108px;top:4718px">Your name*</div>
<div class="field-label" style="left:331px;top:4718px">Your email address*</div>
<div class="field-label" style="left:554px;top:4718px">Your phone (Optional)</div>
<div class="field-line" style="left:108px;top:4746px;width:670px"></div>
<div class="field-label" style="left:108px;top:4775px">Company name (Optional)</div>
<div class="field-label" style="left:331px;top:4775px">Practice Area</div>
<div class="field-label" style="left:554px;top:4775px">Subject (Optional)</div>
<div class="field-line" style="left:108px;top:4803px;width:670px"></div>
<div class="field-label" style="left:108px;top:4840px">Message</div>
<div class="field-line" style="left:108px;top:4930px;width:670px"></div>
<a class="btn" style="left:110px;top:4955px;width:198px;height:42px;font-size:11px">Send Message</a>

<div class="map" role="img" aria-label="Street map showing the office location"></div>

<footer class="footer">
  <div class="abs" style="left:108px;top:78px;font-size:24px;color:#fff">Tallowfield Marsh</div>
  <div class="abs" style="left:150px;top:110px;font-size:10px;color:#c9c9cf">Attorneys at Law</div>
  <div class="foot-small" style="left:350px;top:72px">© 2020 Tallowfield &amp; Marsh LLC.<br>All rights reserved.</div>
  <div class="foot-small" style="left:614px;top:72px">Phone: (555) 010-2141<br><span style="display:block;margin-top:8px">Fax: (555) 010-1257</span><span style="display:block;margin-top:8px;line-height:22px">40 Commerce Plaza Drive Suite<br>312 Riverton, NJ 07000</span></div>
  <div class="abs" style="left:883px;top:113px;width:141px;height:63px;background:#fff;border-radius:2px"></div>
</footer>
<div class="foot-social"><span></span><span></span><span></span><span></span><span></span><span></span></div>

</body>
</html>
```